Window graphics needed for chiropractic office

I am looking to add perforated window vinyl graphic to my exterior office windows. I am looking for something professional and modern and clean and not too busy. I am open to using stock chiropractic photo/s but don't want anything with a spine diagram or person grabbing back in pain. I have included multiple files for you to review some of my ideas. I like the idea of covering all of the bottom windows with a pattern/design that matches my logo colors. (Hex #00pacd and #00ced1). Other complimentary colors are fine too. I have also included several other sample photos and noted what I liked about them. I have also included multiple versions of my logo. I usually use the one with the "Mender Rest Clinic" in dark letters but have one in all white or white letters instead of dark if needed.

Target Market(s)

People recently injured in work and auto accidents and also people seeking wellness care for neck/back pain.

Industry/Entity Type

Healthcare/Chiropractic

Font styles to use
Serif
Sans Serif

Colors
0094D4
00A9DD
6FCCEA
C7EBF8
E9F6FB
00AB8E
00BBA5
67D7C9
C6EFE9
E9F9F6

Requirements
Must have
• See attached photo/diagram of which windows should/should not be covered. Black area must be entirely covered for patient privacy reason. Gray areas can be covered, uncovered or partially covered.
Nice to have
• I am open to having my logo on the windows but not too big since I already have a large LED sign on the opposite wall. Website and phone would be nice: www.vantaheal.example and 314-555-0187. I am open to words listing some of the treats that we offered like "Laser Therapy", "Decompression" , "Chiropractic", "Manual Therapy", "Functional Rehabilitation" , "Auto Accidents", "Work Injuries", "Slip & Fall", "Wellness Care"
Should not have
• Any spine diagrams or person grasping back in pain.

```html
<!DOCTYPE html>
<html lang="en">
<head>
<meta charset="utf-8">
<title>Vantaheal Storefront Window Graphics</title>
<link href="https://fonts.googleapis.com/css2?family=Montserrat:wght@400;700;800&display=swap" rel="stylesheet">
<style>
  :root {
    --frame: #b9b9b9;
    --brand-blue: #0399d3;
    --brand-teal: #16d2d3;
    --teal-light: #6fe3e8;
    --white: #ffffff;
  }
  html, body {
    margin: 0;
    padding: 0;
    width: 1200px;
    height: 600px;
    overflow: hidden;
    background: var(--white);
  }
  .storefront {
    display: block;
    width: 1200px;
    height: 600px;
    font-family: "Montserrat", Arial, sans-serif;
  }
  .frame { fill: var(--frame); }
  .glass { fill: url(#glassShade); }
  .band { fill: var(--brand-blue); }
  .teal-pane { fill: var(--brand-teal); }
  .service-label {
    fill: var(--white);
    font-weight: 700;
    font-size: 24px;
    letter-spacing: 0.5px;
    text-anchor: middle;
  }
  .brand-dot { fill: var(--white); }
  .brand-name { fill: var(--white); font-weight: 700; text-anchor: middle; }
  .brand-sub { fill: var(--white); font-weight: 400; letter-spacing: 0.5px; text-anchor: middle; }
  .phone { fill: var(--white); font-weight: 800; font-size: 66px; }
  .website { fill: var(--white); font-weight: 700; font-size: 38px; }
  .door-glass { fill: var(--white); }
  .handle { fill: none; stroke: #a9a9a9; stroke-width: 5; }
  .inner-frame { fill: none; stroke: #a7a7a7; stroke-width: 10; }
</style>
</head>
<body>
<svg class="storefront" viewBox="0 0 2560 1280" xmlns="http://www.w3.org/2000/svg" role="img" aria-label="Vantaheal clinic storefront window graphics">
  <defs>
    <linearGradient id="glassShade" x1="0" y1="0" x2="1" y2="1">
      <stop offset="0" stop-color="#fafafa"/>
      <stop offset="1" stop-color="#e2e2e2"/>
    </linearGradient>
    <linearGradient id="frameShade" x1="0" y1="0" x2="1" y2="0">
      <stop offset="0" stop-color="#a8a8a8"/>
      <stop offset="0.5" stop-color="#d6d6d6"/>
      <stop offset="1" stop-color="#a8a8a8"/>
    </linearGradient>
    <linearGradient id="privacyFade" x1="0" y1="0" x2="0" y2="1">
      <stop offset="0" stop-color="#13d1d3"/>
      <stop offset="0.6" stop-color="#6fe3e8"/>
      <stop offset="1" stop-color="#0a9ed6"/>
    </linearGradient>
    <clipPath id="privacyPanes">
      <rect x="1214" y="529" width="46" height="257"/>
      <rect x="1270" y="529" width="127" height="257"/>
      <rect x="1407" y="529" width="275" height="257"/>
      <rect x="1692" y="529" width="127" height="257"/>
      <rect x="1829" y="529" width="276" height="257"/>
      <rect x="2115" y="529" width="127" height="257"/>
      <rect x="2252" y="529" width="234" height="257"/>
    </clipPath>
  </defs>

  <rect class="frame" x="77" y="378" width="2421" height="532" fill="url(#frameShade)"/>

  <g class="transom-row">
    <rect class="glass" x="90" y="391" width="127" height="127"/>
    <rect class="glass" x="228" y="391" width="274" height="127"/>
    <rect class="glass" x="513" y="391" width="127" height="127"/>
    <rect class="glass" x="650" y="391" width="275" height="127"/>
    <rect class="glass" x="935" y="391" width="269" height="127"/>
    <rect class="glass" x="1214" y="391" width="46" height="127"/>
    <rect class="glass" x="1270" y="391" width="127" height="127"/>
    <rect class="glass" x="1407" y="391" width="275" height="127"/>
    <rect class="teal-pane" x="1692" y="391" width="127" height="127"/>
    <rect class="brand-dot" x="1737" y="436" width="37" height="37"/>
    <rect class="glass" x="1829" y="391" width="276" height="127"/>
    <rect class="glass" x="2115" y="391" width="127" height="127"/>
    <rect class="teal-pane" x="2252" y="391" width="234" height="127"/>
    <g class="brand-mark">
      <text class="brand-name" x="2369" y="460" font-size="34">Vantaheal</text>
      <text class="brand-sub" x="2369" y="480" font-size="14">MENDER REST CLINIC</text>
    </g>
  </g>

  <g class="main-row">
    <rect class="glass" x="90" y="529" width="127" height="257"/>
    <rect class="glass" x="228" y="529" width="274" height="257"/>
    <rect class="glass" x="513" y="529" width="127" height="257"/>
    <rect class="glass" x="650" y="529" width="275" height="257"/>
  </g>

  <g class="privacy-graphic" clip-path="url(#privacyPanes)" role="img" aria-label="Privacy window graphic in soft teal and blue tones">
    <rect x="1214" y="529" width="1272" height="257" fill="url(#privacyFade)"/>
  </g>
  <rect class="inner-frame" x="1412" y="534" width="265" height="260"/>
  <g class="brand-mark">
    <text class="brand-name" x="1545" y="636" font-size="42">Vantaheal</text>
    <text class="brand-sub" x="1545" y="660" font-size="17">MENDER REST CLINIC</text>
  </g>
  <g class="contact">
    <text class="phone" x="1862" y="635">314-555-0187</text>
    <text class="website" x="1862" y="677">www.vantaheal.example</text>
  </g>

  <g class="entry-doors">
    <rect x="935" y="529" width="269" height="381" fill="url(#frameShade)"/>
    <rect class="door-glass" x="958" y="552" width="88" height="310"/>
    <rect class="door-glass" x="1093" y="552" width="88" height="310"/>
    <path class="handle" d="M1055 708 L1046 708 Q1040 708 1040 714 L1040 740 Q1040 746 1046 746 L1055 746"/>
    <path class="handle" d="M1084 708 L1093 708 Q1099 708 1099 714 L1099 740 Q1099 746 1093 746 L1084 746"/>
  </g>

  <g class="service-band">
    <rect class="band" x="90" y="796" width="127" height="100"/>
    <rect class="brand-dot" x="135" y="828" width="37" height="37"/>
    <rect class="band" x="228" y="796" width="274" height="100"/>
    <text class="service-label" x="366" y="856">DECOMPRESSION</text>
    <rect class="band" x="513" y="796" width="127" height="100"/>
    <rect class="brand-dot" x="558" y="828" width="37" height="37"/>
    <rect class="band" x="650" y="796" width="275" height="100"/>
    <text class="service-label" x="787" y="856">CHIROPRACTIC</text>
    <rect class="band" x="1214" y="796" width="46" height="100"/>
    <rect class="band" x="1270" y="796" width="127" height="100"/>
    <rect class="brand-dot" x="1315" y="828" width="37" height="37"/>
    <rect class="band" x="1407" y="796" width="275" height="100"/>
    <text class="service-label" x="1540" y="856">LASER THERAPY</text>
    <rect class="band" x="1692" y="796" width="127" height="100"/>
    <rect class="brand-dot" x="1737" y="828" width="37" height="37"/>
    <rect class="band" x="1829" y="796" width="276" height="100"/>
    <text class="service-label" x="1966" y="856">MANUAL THERAPY</text>
    <rect class="band" x="2115" y="796" width="127" height="100"/>
    <rect class="brand-dot" x="2160" y="828" width="37" height="37"/>
    <rect class="band" x="2252" y="796" width="234" height="100"/>
    <text class="service-label" x="2369" y="856">WELLNESS CARE</text>
  </g>
</svg>
</body>
</html>
```